BrindleStaffing Business Card Design

We are a staffing company finding positions for dedicated nurses and physicians.

Target Market(s)

Business Professionals

Industry/Entity Type

Staffing

Contact Information for Business Card

Gregory Malden
Chairman
417 39th Crescent South
SAINT PETERSBURG FL 33719
813-555-0147 Mobile
813-555-0183 Fax
gmalden@brindlestaffing.example
www.brindlestaffing.example

Font styles to use
Sans Serif

Colors
fbee3e
f04a50
f37122

Requirements
Must have
• Logo Attached, see colors below. We'd like to see Yellow, Orange and Red.

```html
<!DOCTYPE html>
<html lang="en">
<head>
<meta charset="utf-8">
<title>BrindleStaffing Business Card</title>
<link rel="stylesheet" href="https://fonts.googleapis.com/css2?family=Nunito:wght@800&family=Lato:wght@400;700&display=swap">
<style>
  :root {
    --backdrop: #dcdcdc;
    --backdrop-light: #e9e9e9;
    --brand-yellow: #fbee3e;
    --brand-red: #f04a50;
    --brand-orange: #f37122;
    --card-white: #ffffff;
    --ink: #2b2b2b;
    --ink-soft: #6b6b6b;
    --card-shadow: rgba(0, 0, 0, 0.22);
  }
  * { box-sizing: border-box; margin: 0; padding: 0; }
  html, body {
    width: 1200px;
    height: 900px;
    overflow: hidden;
  }
  body {
    background: radial-gradient(ellipse at 50% 35%, var(--backdrop-light), var(--backdrop));
    position: relative;
    font-family: "Lato", Arial, sans-serif;
  }
  .card {
    position: absolute;
    width: 560px;
    height: 320px;
    border-radius: 28px;
    overflow: hidden;
    box-shadow: 0 14px 28px var(--card-shadow), 0 2px 5px var(--card-shadow);
  }

  /* Front side */
  .card-front {
    left: 70px;
    top: 90px;
    background: linear-gradient(160deg, var(--brand-red) 0%, var(--brand-red) 20%, var(--brand-orange) 65%, #f7a12e 100%);
    display: flex;
    align-items: center;
    justify-content: center;
  }
  .front-wordmark {
    font-family: "Nunito", "Lato", sans-serif;
    font-weight: 800;
    font-size: 54px;
    color: var(--card-white);
    letter-spacing: 0.3px;
  }

  /* Back side */
  .card-back {
    left: 570px;
    top: 480px;
    background: var(--card-white);
  }
  .back-wordmark {
    position: absolute;
    left: 40px;
    top: 50px;
    font-family: "Nunito", "Lato", sans-serif;
    font-weight: 800;
    font-size: 48px;
    line-height: 1;
    color: var(--brand-red);
  }
  .holder-name {
    position: absolute;
    left: 40px;
    top: 122px;
    font-family: "Nunito", "Lato", sans-serif;
    font-weight: 800;
    font-size: 27px;
    line-height: 1;
  }
  .holder-name .first { color: var(--brand-orange); }
  .holder-name .last { color: var(--brand-red); }
  .holder-title {
    position: absolute;
    left: 40px;
    top: 155px;
    font-size: 15px;
    color: var(--ink-soft);
    letter-spacing: 0.5px;
  }
  .contact-list {
    position: absolute;
    left: 40px;
    top: 196px;
    list-style: none;
    font-size: 15px;
    line-height: 22px;
    color: var(--ink);
  }
  .contact-list li {
    display: flex;
    align-items: center;
    gap: 8px;
  }
  .contact-list svg { width: 13px; height: 13px; fill: var(--brand-orange); flex: none; }
  .contact-list .label { color: var(--ink-soft); }
  .contact-web .web-lead { color: var(--brand-orange); }
  .contact-web .web-tail { color: var(--brand-red); }
  .address {
    position: absolute;
    right: 32px;
    top: 196px;
    text-align: right;
    font-size: 15px;
    line-height: 22px;
    color: var(--ink);
    font-style: normal;
  }
  .address .city { text-transform: uppercase; }
  .edge-band {
    position: absolute;
    left: 0;
    right: 0;
    bottom: 0;
    height: 14px;
    display: flex;
  }
  .edge-band .band-red { flex: 1; background: var(--brand-red); }
  .edge-band .band-orange { flex: 1; background: var(--brand-orange); }
  .edge-band .band-yellow { flex: 1; background: var(--brand-yellow); }
</style>
</head>
<body>
  <section class="card card-front" aria-label="Card front">
    <span class="front-wordmark">BrindleStaffing</span>
  </section>

  <section class="card card-back" aria-label="Card back">
    <div class="back-wordmark">BrindleStaffing</div>
    <div class="holder-name"><span class="first">Gregory</span> <span class="last">Malden</span></div>
    <div class="holder-title">Chairman</div>
    <ul class="contact-list">
      <li class="contact-phone">
        <svg viewBox="0 0 24 24" aria-hidden="true"><path d="M6.6 10.8a15.1 15.1 0 0 0 6.6 6.6l2.2-2.2a1 1 0 0 1 1-.25 11.4 11.4 0 0 0 3.6.57 1 1 0 0 1 1 1V20a1 1 0 0 1-1 1A17 17 0 0 1 3 4a1 1 0 0 1 1-1h3.5a1 1 0 0 1 1 1c0 1.25.2 2.45.57 3.57a1 1 0 0 1-.25 1z"/></svg>
        <span>813-555-0147 <span class="label">Mobile</span></span>
      </li>
      <li class="contact-fax">
        <svg viewBox="0 0 24 24" aria-hidden="true"><path d="M6 2h12v6H6z M2 9h20v9h-4v4H6v-4H2z M8 15v5h8v-5z" fill-rule="evenodd"/></svg>
        <span>813-555-0183 <span class="label">Fax</span></span>
      </li>
      <li class="contact-email">
        <svg viewBox="0 0 24 24" aria-hidden="true"><path d="M2 5h20v14H2z M3.5 6.5v.4l8.5 5.6 8.5-5.6v-.4z" fill-rule="evenodd"/></svg>
        gmalden@brindlestaffing.example
      </li>
      <li class="contact-web">
        <svg viewBox="0 0 24 24" aria-hidden="true"><circle cx="12" cy="12" r="10"/></svg>
        <span><span class="web-lead">www.brindlestaffing</span><span class="web-tail">.example</span></span>
      </li>
    </ul>
    <address class="address">
      417 39th Crescent South<br>
      <span class="city">Saint Petersburg FL 33719</span>
    </address>
    <div class="edge-band" aria-hidden="true">
      <span class="band-red"></span>
      <span class="band-orange"></span>
      <span class="band-yellow"></span>
    </div>
  </section>
</body>
</html>
```